Email footer project

We are looking for a standardised email footer that can be changed monthly for various project we are working on.
Please refer to EMAIL FOOTER BRIEF FOR ALL INFORMATION

We have uploaded some previous footers as a sample.

Target Market(s)

property, environmental

Industry/Entity Type

energy and property

Colors
00AB8E
00BBA5
67D7C9
C6EFE9
E9F9F6

Requirements
Must have
• company branding - verdalith.co.uk.

```html
<!DOCTYPE html>
<html lang="en">
<head>
<meta charset="utf-8">
<title>Email Footer – Delivering Net Zero</title>
<link rel="stylesheet" href="https://fonts.googleapis.com/css2?family=Arimo:wght@400;700&family=Open+Sans:wght@400&display=swap">
<style>
  :root {
    --page-bg: #ffffff;
    --label-ink: #231f20;
    --teal-mist: #E9F9F6;
    --teal-pale: #C6EFE9;
    --teal-light: #67D7C9;
    --teal-bright: #00BBA5;
    --teal-core: #00AB8E;
    --teal-deep: #00705d;
    --white: #ffffff;
    --button-ink: #003d33;
  }
  html, body {
    margin: 0;
    padding: 0;
    width: 1200px;
    height: 1000px;
    overflow: hidden;
    background: var(--page-bg);
  }
  .canvas {
    position: relative;
    width: 1200px;
    height: 1000px;
  }
  .edition-label {
    position: absolute;
    left: 100px;
    top: 413px;
    margin: 0;
    font-family: "Open Sans", sans-serif;
    font-weight: 400;
    font-size: 24px;
    color: var(--label-ink);
  }
  .footer-banner {
    position: absolute;
    left: 100px;
    top: 459px;
    width: 1000px;
    height: 125px;
  }
  .banner-shapes {
    position: absolute;
    inset: 0;
  }
  .banner-headline {
    position: absolute;
    left: 50px;
    top: 13px;
    margin: 0;
    font-family: "Arimo", sans-serif;
    font-weight: 700;
    font-size: 36px;
    line-height: 47px;
    letter-spacing: 0.4px;
    color: var(--teal-deep);
  }
  .banner-message {
    position: absolute;
    left: 392px;
    top: 14px;
    margin: 0;
    font-family: "Arimo", sans-serif;
    font-weight: 400;
    font-size: 24.5px;
    line-height: 30.5px;
    color: var(--white);
  }
  .learn-more {
    position: absolute;
    left: 773px;
    top: 32px;
    width: 181px;
    height: 52px;
    border-radius: 12px;
    background: var(--white);
    display: flex;
    align-items: center;
    justify-content: center;
    font-family: "Arimo", sans-serif;
    font-weight: 700;
    font-size: 17.5px;
    letter-spacing: 0.4px;
    color: var(--button-ink);
    text-decoration: none;
  }
  .brand-name {
    position: absolute;
    left: 773px;
    top: 94px;
    width: 181px;
    margin: 0;
    text-align: center;
    font-family: "Arimo", sans-serif;
    font-weight: 700;
    font-size: 13px;
    letter-spacing: 0.5px;
    color: var(--white);
  }
</style>
</head>
<body>
<div class="canvas">
  <p class="edition-label">April 2022</p>

  <section class="footer-banner">
    <svg class="banner-shapes" width="1000" height="125" viewBox="0 0 1000 125">
      <defs>
        <clipPath id="chevron-clip">
          <polygon points="317,0 712.6,0 735.4,65.7 715.4,125 320,125 340,65.7"/>
        </clipPath>
        <radialGradient id="globe-glow" cx="0.55" cy="0.5" r="0.6">
          <stop offset="0" stop-color="#67D7C9" stop-opacity="0.55"/>
          <stop offset="0.6" stop-color="#00BBA5" stop-opacity="0.35"/>
          <stop offset="1" stop-color="#00AB8E" stop-opacity="0"/>
        </radialGradient>
      </defs>
      <rect x="0" y="0" width="1000" height="125" fill="var(--teal-bright)"/>
      <rect x="0" y="0" width="340" height="125" fill="var(--teal-mist)"/>
      <polygon class="panel-chevron" points="317,0 712.6,0 735.4,65.7 715.4,125 320,125 340,65.7" fill="var(--teal-core)"/>
      <g clip-path="url(#chevron-clip)" role="img" aria-label="Photo of planet Earth in teal tones fading into the panel">
        <ellipse cx="655" cy="72" rx="120" ry="95" fill="url(#globe-glow)"/>
      </g>
    </svg>

    <h2 class="banner-headline">DELIVERING<br>NET ZERO</h2>
    <p class="banner-message">Are you ready for EPC<br>legislation changes in<br>April 2023?</p>
    <a class="learn-more" href="#">LEARN MORE</a>
    <p class="brand-name">verdalith.co.uk</p>
  </section>
</div>
</body>
</html>
```